New profile page for existing party website

For the party website 'Revelmap' we need a new design for the user profile page.

The page should show
* a profile picture
* basic information like name, age and city
* music styles he/she likes
* links to their Chatterly profile and website
* a bio (HTML content)
* events they plan to go to
* past events
* pictures

Challenge is that some users may have little information (just their name) while others have a huge description, lots of foto's, events, etc.

Please visit http://www.revelmap.example and http://www.revelmap.example/users/gordon

Target Market(s)

Men and women between 18 and 35

Industry/Entity Type

Night Club

Number of Pages Required

2 page

Font styles to use
Other font styles liked:
• Roboto

Requirements
Must have
• Please design how the page looks with a fully filled out profile and with an empty profile.
• It should fit well with the existing website.
• Include designs for both for small screens (mobile) and large screens (tablet, desktop).
Nice to have
• UX design on how to collapse or paginate sections.
• Interactive effects would be a bonus.
Should not have
• The page should not have subnavigation like menus or tabs.

```html
<!DOCTYPE html>
<html lang="nl">
<head>
<meta charset="utf-8">
<title>RobinK Photography – Revelmap</title>
<link href="https://fonts.googleapis.com/css2?family=Roboto:ital,wght@0,300;0,400;0,500;0,700;1,400&family=Lato:ital,wght@0,400;0,700;1,400&display=swap" rel="stylesheet">
<style>
:root{
  --black:#0b0b0b;
  --hero:#262626;
  --hero-dark:#1c1c1c;
  --white:#ffffff;
  --page:#ffffff;
  --card:#f7f7f7;
  --card-border:#dedede;
  --text:#666666;
  --heading:#222222;
  --line:#d9d9d9;
  --gallery-bg:#f3f3f3;
  --accent:#2f2f2f;
}
*{box-sizing:border-box;margin:0;padding:0}
html,body{width:1200px;height:2387px;overflow:hidden}
body{position:relative;background:var(--page);font-family:'Lato',sans-serif;color:var(--text)}
.abs{position:absolute}

/* top navigation */
.topbar{left:0;top:0;width:1200px;height:57px;background:var(--black)}
.brand{left:132px;top:12px;font-family:'Roboto',sans-serif;font-weight:700;font-size:26px;color:var(--white);line-height:32px}
.nav-item{top:18px;font-family:'Roboto',sans-serif;font-size:16px;line-height:20px;color:#cfcfcf;white-space:nowrap}
.search{left:777px;top:13px;width:135px;height:32px;background:var(--white);border-radius:2px;font-family:'Roboto',sans-serif;font-size:13px;color:#aaa;padding:7px 10px}
.nav-divider{left:931px;top:8px;width:1px;height:42px;background:#444}
.account{left:950px;top:10px;width:118px;height:39px;border:1px solid #bdbdbd;border-radius:4px;color:var(--white);font-family:'Roboto',sans-serif;font-size:15px;text-align:center;line-height:37px}

/* profile header */
.hero{left:0;top:57px;width:1200px;height:325px;background:linear-gradient(135deg,var(--hero),var(--hero-dark))}
.avatar{left:150px;top:100px;width:236px;height:238px;border:2px solid #e6e6e6;background:linear-gradient(160deg,#a47c63,#6d4b38 60%,#3f3a36)}
.profile-name{left:423px;top:90px;font-family:'Roboto',sans-serif;font-size:45px;line-height:56px;color:var(--white);font-weight:400}
.facts{left:424px;top:159px;color:var(--white);font-family:'Roboto',sans-serif}
.fact{height:32px;display:flex;align-items:baseline;gap:10px;line-height:28px}
.fact dt{font-size:20px}
.fact dd{font-size:14px;color:#eaeaea}
.socials{left:421px;top:303px;display:flex;gap:8px}
.socials svg{display:block}

/* content cards */
.card{left:132px;width:938px;background:var(--card);border:1px solid var(--card-border);box-shadow:0 4px 10px rgba(0,0,0,.06);padding:30px 22px 0 22px}
.card h2{font-family:'Roboto',sans-serif;font-weight:400;font-size:24px;line-height:30px;color:var(--heading);margin-bottom:8px}
.card p{font-size:16.2px;line-height:25.5px;letter-spacing:.15px}
.card .rules{letter-spacing:.8px}
.card a{color:var(--heading);text-decoration:none}

/* events */
.section-title{font-family:'Roboto',sans-serif;font-weight:500;font-size:27px;line-height:32px;color:var(--heading)}
.read-all{font-family:'Roboto',sans-serif;font-style:italic;font-size:13px;color:#333}
.rule{height:1px;background:var(--line)}
.rule-accent{height:3px;background:#bcbcbc}
.col-divider{left:598px;top:1622px;width:1px;height:264px;background:var(--line)}
.event-thumb{width:129px;height:111px;border:1px solid #ddd;background:linear-gradient(150deg,#c9b49b,#d88a3a 55%,#8f7c6a)}
.event-body{width:290px}
.event-meta{font-family:'Roboto',sans-serif;font-style:italic;font-size:13px;color:#444}
.event-title{font-family:'Roboto',sans-serif;font-weight:500;font-size:15.5px;color:#111;margin-top:12px;letter-spacing:.3px}
.event-text{font-family:'Roboto',sans-serif;font-size:13px;line-height:20px;color:#444;margin-top:8px}
.acc{left:630px;width:438px;border:1px solid #cfcfcf;background:#eeeeee;border-radius:2px}
.acc-head{height:38px;display:flex;align-items:center;padding:0 12px;font-family:'Roboto',sans-serif;font-size:14.5px;color:#222;gap:10px}
.acc-head .date{margin-left:auto;font-style:italic;font-size:13px}
.acc.open{background:var(--white)}
.acc.open .acc-head{background:var(--accent);color:var(--white);margin:3px;border-radius:2px;height:36px}
.acc-body{padding:8px 14px;font-size:12.5px;line-height:19px;color:#777}

/* gallery */
.gallery{left:0;top:1935px;width:1200px;height:374px;background:var(--gallery-bg)}
.gallery-title{left:0;top:1970px;width:1200px;text-align:center;font-family:'Roboto',sans-serif;font-weight:500;font-size:27px;color:var(--heading)}
.gallery-rule{left:415px;top:2015px;width:370px;height:1px;background:#ddd}
.shot{top:2039px;width:178px;height:177px}

/* footer */
.footer{left:0;top:2309px;width:1200px;height:78px;background:var(--black)}
.footer-links{left:0;top:2333px;width:1200px;text-align:center;font-family:'Roboto',sans-serif;font-weight:700;font-size:12.5px;color:var(--white);letter-spacing:.3px}
.copyright{left:0;top:2364px;width:1200px;text-align:center;font-family:'Roboto',sans-serif;font-size:10px;color:#ddd}
</style>
</head>
<body>

<header class="abs topbar"></header>
<div class="abs brand">Revelmap</div>
<nav>
  <span class="abs nav-item" style="left:399px">Home</span>
  <span class="abs nav-item" style="left:463px">Agenda</span>
  <span class="abs nav-item" style="left:530px">Vrijkaarten</span>
  <span class="abs nav-item" style="left:640px">Foto's</span>
  <span class="abs nav-item" style="left:701px">Nieuws</span>
</nav>
<div class="abs search">Zoeken</div>
<div class="abs nav-divider"></div>
<div class="abs account">Mijn account</div>

<section class="abs hero"></section>
<div class="abs avatar" role="img" aria-label="Profielfoto van de fotograaf"></div>
<h1 class="abs profile-name">RobinK Photography</h1>
<dl class="abs facts">
  <div class="fact"><dt>Function:</dt><dd>Head promotions, photograper, communication, marketing, and sales.</dd></div>
  <div class="fact"><dt>Music Styles:</dt><dd>Classical Music , Romantic , Traditional Music , Popular Music</dd></div>
  <div class="fact"><dt>Active since:</dt><dd>jan 2006</dd></div>
  <div class="fact"><dt>Shoots:</dt><dd>500 and counting</dd></div>
</dl>
<div class="abs socials">
  <svg width="30" height="30" viewBox="0 0 30 30" aria-label="Chatterly"><circle cx="15" cy="15" r="14" fill="#fff"/></svg>
  <svg width="30" height="30" viewBox="0 0 30 30" aria-label="Website"><circle cx="15" cy="15" r="14" fill="#fff"/><g fill="none" stroke="#333" stroke-width="1.4"><circle cx="15" cy="15" r="9"/><ellipse cx="15" cy="15" rx="4" ry="9"/><line x1="6" y1="15" x2="24" y2="15"/><line x1="8" y1="10" x2="22" y2="10"/><line x1="8" y1="20" x2="22" y2="20"/></g></svg>
  <svg width="30" height="30" viewBox="0 0 30 30" aria-label="E-mail"><circle cx="15" cy="15" r="14" fill="#fff"/><rect x="8" y="10" width="14" height="10" rx="1" fill="#333"/><polyline points="8.5,10.5 15,16 21.5,10.5" fill="none" stroke="#fff" stroke-width="1.3"/></svg>
</div>

<article class="abs card" style="top:426px;height:215px">
  <h2>Wil jij fotograferen voor Revelmap?</h2>
  <p>Als je uitgaan leuk vindt, makkelijk bent in de omgang en uiteraard houdt van fotograferen, biedt Revelmap je de kans een kijkje te nemen in de wereld van de partyfotografie. Door de inzet van de fotografen is Revelmap uitgegroeid tot een van de meest toonaangevende partysites van Nederland. De betrouwbaarheid, de hoge kwaliteit van de foto's en het coveren van de belangrijkste evenementen maakt van Revelmap een van de best bezochte websites in ons vakgebied.</p>
</article>

<article class="abs card" style="top:677px;height:269px">
  <h2>Belangrijk informatie</h2>
  <p>Fotograferen voor Revelmap is op vrijwillige basis. Je kan kiezen waar en wanneer je uitgaat en foto's maakt, maar een vaste inbreng word wel van je verwacht. Hoe meer je voor Revelmap doet, hoe meer ervaring je opdoet met de camera en hoe beter je word. Hierdoor kan je weer naar interessantere feesten en festivals. Wat je wel krijgt is gratis entree voor een evenement en soms ook andere voordelen zoals gratis drankjes... Je gaat meestal met ze tweetjes op pad en ontmoet veel nieuwe mensen zoals DJ's en organisatoren. Hoe meer je voor Revelmap.example werkt hoe meer ervaring je er ook uit zal halen. De beste fotografen doen de leukste en de meest uitdagende evenementen bijvoorbeeld: Aurora Hall, Pulse Outdoor, Sunray weekend, Harbor Dance etc.</p>
</article>

<article class="abs card" style="top:981px;height:246px">
  <h2>Voorwaarden</h2>
  <p class="rules">- Je moet 18 jaar of ouder zijn.<br>- Je moet het aankunnen om hoge kwaliteit foto's te maken en professioneel gedrag vertonen.<br>- Je moet sociaal zijn; een open persoon zijn die ervan houdt om andere mensen te ontmoeten.<br>- Het is een vereiste dat je een digitale spiegelreflex-camera hebt en lichtsterke lens met vast diafragma van F2.8 en natuurlijk een externe flitser (E-TTL).<br>- Je bent verantwoordelijk voor je eigen vervoer om naar de evenementen te gaan waar je foto's maakt.</p>
</article>

<article class="abs card" style="top:1263px;height:236px">
  <h2>Aanmelden</h2>
  <p>Wil jij ook het team van Revelmap versterken en het nachtleven van een andere kant verkennen? Geef je dan op, stuur een mailtje naar <a href="mailto:robin@revelmap.example">robin@revelmap.example</a> Vermeld daar goed in je naam, leeftijd, woonplaats en het type camera dat je hebt en je ervaring op het gebied van fotograferen.</p>
  <p style="margin-top:6px">Bekijk ons online foto album voor de door mij geschoten foto's. Bekijk al mijn Clipstream filmpjes via mijn eigen Clipstream kanaal<br><a href="#">www.clipstream.example/user/1982RobinK</a></p>
</article>

<h3 class="abs section-title" style="left:134px;top:1563px">Upcoming Events</h3>
<div class="abs read-all" style="left:459px;top:1577px">Read All Events <b>»</b></div>
<div class="abs rule" style="left:132px;top:1603px;width:441px"></div>
<div class="abs rule-accent" style="left:132px;top:1602px;width:66px"></div>

<div class="abs event-thumb" style="left:132px;top:1622px" role="img" aria-label="Foto van feestgangers bij een evenement"></div>
<div class="abs event-body" style="left:283px;top:1620px">
  <div class="event-meta">23 Apr 2016 &nbsp; / &nbsp; 0 Comments</div>
  <div class="event-title">LOREM IPSUM DOLOR &nbsp;CONSECTE</div>
  <div class="event-text">Duis autem vel eum iriure dolor in hendreri inmo vulputate velit esse molestie consequatn vel illum dolore eu feugiat nulla facilisis... [+]</div>
</div>
<div class="abs rule" style="left:283px;top:1752px;width:290px"></div>
<div class="abs event-thumb" style="left:132px;top:1771px" role="img" aria-label="Foto van feestgangers bij een evenement"></div>
<div class="abs event-body" style="left:283px;top:1770px">
  <div class="event-meta">24 Apr 2016 &nbsp; / &nbsp; 0 Comments</div>
  <div class="event-title">LOREM IPSUM DOLOR &nbsp;CONSECTE</div>
  <div class="event-text">Duis autem vel eum iriure dolor in hendreri inmo vulputate velit esse molestie consequatn vel illum dolore eu feugiat nulla facilisis... [+]</div>
</div>

<div class="abs col-divider"></div>

<h3 class="abs section-title" style="left:631px;top:1563px">Past Events</h3>
<div class="abs read-all" style="left:965px;top:1577px">Sea All Events <b>»</b></div>
<div class="abs rule" style="left:630px;top:1603px;width:438px"></div>
<div class="abs rule-accent" style="left:630px;top:1602px;width:66px"></div>

<div class="abs acc open" style="top:1622px;height:94px">
  <div class="acc-head"><span>—</span><span>Ut wisi enim ad minim ve quis nostrud</span><span class="date">20 Apr 2016</span></div>
  <div class="acc-body">Sed risus urna, ultricies sed ultricies in, interdum nec odio Nulla e eska nunc tristique pretium. Mauris non ornare neque.</div>
</div>
<div class="abs acc" style="top:1727px"><div class="acc-head"><b>+</b><span>Ut wisi enim ad minim ve quis nostrud</span><span class="date">19 Mar 2016</span></div></div>
<div class="abs acc" style="top:1784px"><div class="acc-head"><b>+</b><span>Ut wisi enim ad minim ve quis nostrud</span><span class="date">10 Mar 2016</span></div></div>
<div class="abs acc" style="top:1840px"><div class="acc-head"><b>+</b><span>Ut wisi enim ad minim ve quis nostrud</span><span class="date">26 Feb 2016</span></div></div>

<section class="abs gallery"></section>
<h3 class="abs gallery-title">Gallery</h3>
<div class="abs gallery-rule"></div>
<div class="abs shot" style="left:132px;background:linear-gradient(160deg,#5a2a6e,#9b3f7a 50%,#2a1e2f)" role="img" aria-label="Feestfoto: bezoekers op de dansvloer"></div>
<svg class="abs" style="left:205px;top:2112px" width="32" height="32" viewBox="0 0 32 32" aria-hidden="true"><circle cx="13" cy="13" r="9" fill="none" stroke="#fff" stroke-width="2.4"/><line x1="20" y1="20" x2="28" y2="28" stroke="#fff" stroke-width="3"/><line x1="9" y1="13" x2="17" y2="13" stroke="#fff" stroke-width="2"/><line x1="13" y1="9" x2="13" y2="17" stroke="#fff" stroke-width="2"/></svg>
<div class="abs shot" style="left:322px;background:linear-gradient(160deg,#3d2624,#7d5a4a 50%,#2b1b1a)" role="img" aria-label="Feestfoto: groep vrienden in een club"></div>
<div class="abs shot" style="left:511px;background:linear-gradient(160deg,#1e1e1e,#6a5a4a 50%,#111)" role="img" aria-label="Feestfoto: bezoekers poseren samen"></div>
<div class="abs shot" style="left:702px;background:linear-gradient(160deg,#1a1414,#8a5a48 50%,#200f10)" role="img" aria-label="Feestfoto: drie vriendinnen op een feest"></div>
<div class="abs shot" style="left:891px;background:linear-gradient(160deg,#1a1a2a,#6a4a3a 50%,#7a1a1a)" role="img" aria-label="Feestfoto: twee feestgangers poseren"></div>
<svg class="abs" style="left:568px;top:2240px" width="66" height="34" viewBox="0 0 66 34" aria-label="Vorige en volgende">
  <circle cx="16" cy="16" r="13" fill="#fff" stroke="#aaa" stroke-width="2"/><path d="M21 16H10M14 11l-5 5 5 5" fill="none" stroke="#aaa" stroke-width="2.4"/>
  <circle cx="49" cy="16" r="13" fill="#fff" stroke="#222" stroke-width="2"/><path d="M43 16h11M50 11l5 5-5 5" fill="none" stroke="#222" stroke-width="2.4"/>
</svg>

<footer class="abs footer"></footer>
<div class="abs footer-links">CONTACT &nbsp;| &nbsp; GEBRUIKERSVOORWAARDEN &nbsp;| &nbsp; PRIVACY POLICY</div>
<div class="abs copyright">© 2004 - 2016 Revelmap</div>

</body>
</html>
```